AMAZING BLACK FRIDAY AD FOR PRINT OR THE WEB

Create a Black Friday ad for nitrile gloves. We are offering a box of 100, no-powder, exam grade nitrile gloves, for $9.99. No limit. Each case is $99. Create something simple, eye catching, cool. KestrelWrap.com. Sale ends on December 4th. While supplies last. We are a local medical supply company in Hawaii that serves the general public in addition to local businesses, government, etc. Gloves are in short supply and we have tons of inventory ready to sell.

Target Market(s)

Businesses that use supplies such as gloves

Industry/Entity Type

medical supplies

Requirements
Must have
• logo and website

```html
<!DOCTYPE html>
<html lang="en">
<head>
<meta charset="utf-8">
<title>Black Friday Sale – Nitrile Gloves – KestrelWrap.com</title>
<link rel="stylesheet" href="https://fonts.googleapis.com/css2?family=Inter:wght@300;400;700;800&display=swap">
<style>
  :root {
    --page-bg: #ffffff;
    --ad-bg: #ffffff;
    --ink: #000000;
    --brand-grey: #6d6e70;
    --brand-green: #1f9a3c;
    --glove-light: #7cc3ec;
    --glove-mid: #3b9fdc;
    --glove-dark: #1f7fc0;
  }
  * { margin: 0; padding: 0; box-sizing: border-box; }
  html, body {
    width: 1200px; height: 1000px; overflow: hidden;
    background: var(--page-bg);
    font-family: "Inter", Arial, sans-serif;
    color: var(--ink);
  }
  .ad {
    position: absolute; left: 168px; top: 68px;
    width: 864px; height: 864px;
    background: var(--ad-bg);
    overflow: hidden;
  }
  .ad > * { position: absolute; }
  .headline {
    left: 0; width: 864px; top: 27px;
    text-align: center; line-height: 1;
    font-weight: 700; font-size: 60px; letter-spacing: -0.5px;
  }
  .product-title {
    left: 0; width: 864px; top: 94px;
    text-align: center; line-height: 1;
    font-weight: 300; font-size: 97px; letter-spacing: -1.5px;
  }
  .glove-photo {
    left: 14px; top: 205px; width: 370px; height: 659px;
    border-radius: 170px 180px 0 0;
    background: radial-gradient(ellipse at 45% 40%, var(--glove-light), var(--glove-mid) 55%, var(--glove-dark));
  }
  .price {
    left: 0; top: 0; width: 864px; height: 400px;
    font-weight: 800; line-height: 1;
  }
  .price > span { position: absolute; white-space: nowrap; }
  .price .currency { left: 414px; top: 201px; font-size: 130px; letter-spacing: -2px; }
  .price .dollars { left: 490px; top: 197px; font-size: 185px; }
  .price .dot { left: 612px; top: 332px; width: 18px; height: 18px; background: var(--ink); }
  .price .cents { left: 622px; top: 206px; font-size: 140px; letter-spacing: -6px; }
  .price .unit { left: 660px; top: 331px; font-weight: 400; font-size: 22px; letter-spacing: 2px; }
  .product-detail {
    left: 405px; width: 400px; top: 364px;
    text-align: center; font-size: 28px; line-height: 34px;
  }
  .terms {
    left: 380px; width: 460px; top: 476px;
    text-align: center; font-weight: 700; font-size: 30px; line-height: 40px;
  }
  .brand {
    left: 420px; width: 380px; top: 640px;
    display: flex; flex-direction: column; align-items: center; gap: 24px;
  }
  .brand-dot { width: 70px; height: 70px; border-radius: 50%; background: var(--brand-green); }
  .brand-name { font-weight: 800; font-size: 46px; letter-spacing: -1px; color: var(--brand-grey); }
</style>
</head>
<body>
  <main class="ad">
    <h1 class="headline">Amazing Black Friday Sale</h1>
    <h2 class="product-title">100 Nitrile Gloves</h2>
    <div class="glove-photo" role="img" aria-label="Photo of a hand wearing a blue nitrile exam glove"></div>
    <div class="price" aria-label="$9.99 per box">
      <span class="currency">$</span>
      <span class="dollars">9</span>
      <span class="dot"></span>
      <span class="cents">99</span>
      <span class="unit">per box</span>
    </div>
    <p class="product-detail">no-powder, exam grade<br>nitrile gloves</p>
    <p class="terms">No limit. Each case is $99.<br>Sale ends on December 4th.<br>While supplies last.</p>
    <div class="brand">
      <span class="brand-dot"></span>
      <span class="brand-name">KestrelWrap.com</span>
    </div>
  </main>
</body>
</html>
```